High-End Residential and Commercial Appliance Repair Redesign (Winnipeg)

Full redesign and migration of https://tallpineappliancecare.ca from Divi to Kadence WP (Gutenberg).

Technical requirements:

Performance: Mobile PageSpeed Insights score must be 90+.

Framework: Use Kadence Theme and Kadence Blocks only. No heavy builders or extra plugins.

SEO: 1:1 migration of all existing URL slugs, H1-H3 headers, and meta-data.

Architecture: All styles must be managed via Kadence Customizer (Global Palette and Typography).

New pages and content expansion:
The designer must create new dedicated landing pages for the following services:

Commercial Reach-in Refrigeration: Prep tables and beverage coolers only. No walk-in units.

Commercial Dishwashers: Professional undercounter, hood-type, and conveyor units.

Commercial Laundry: High-capacity professional washers and dryers.

Commercial Electric Ovens: Professional ranges and convection ovens. No gas equipment.

Residential Brands: Individual pages for Frostline, Brann, Lumo, Tessa, and Halden.

Homepage structure:
The homepage must feature a dual-entry hero section to clearly separate Residential and Commercial clients.

Maintenance and handover:
The site must be built using professional standards for future maintenance by web developers. Documentation on site architecture is required upon completion.

Target Market(s)

Homeowners in Winnipeg seeking premium repair for luxury appliance brands (Frostline, Brann, Tessa), AND local business managers (restaurants, hotels, care homes) needing urgent repair for commercial electric kitchen and laundry equipment.

Industry/Entity Type

Appliance Repair Services

Coding

Coded - Design and coding required

Number of Pages Required

5+ page

Requirements
Must have
• Built strictly on Kadence WP Theme and Gutenberg Blocks. Mobile PageSpeed Insights score of 90+. Clear dual-entry homepage separating Residential and Commercial clients.
Nice to have
• Modular block design for easy future scaling. Premium visual aesthetic for luxury residential brands. Solid, highly professional B2B layout for commercial pages. Clear UI placeholders for future trust badges and company benefits.
Should not have
• Strictly NO AI-generated images and NO generic, cheap-looking stock photography. AI and standard free stock images look unnatural and destroy the premium, trustworthy standard of our brand. Use ONLY highly authentic, premium-grade imagery, or use clean placeholders (e.g., solid color blocks) where we will later insert the client's actual real-life photos.

```html
<!DOCTYPE html>
<html lang="en">
<head>
<meta charset="utf-8">
<title>Tall Pine Appliance Care – Appliance Repair in Winnipeg</title>
<link rel="stylesheet" href="https://fonts.googleapis.com/css2?family=Montserrat:wght@400;500;600;700;800&display=swap">
<style>
:root{
  --red:#e31e24;
  --ink:#1b1b1b;
  --dark:#171717;
  --grey-bg:#f3f3f3;
  --line:#dcdcdc;
  --white:#fff;
  --brand-ink:#2e3a4e;
}
*{box-sizing:border-box;margin:0;padding:0}
html,body{width:1200px;height:4067px;overflow:hidden}
body{font-family:"Montserrat",sans-serif;color:var(--ink);background:var(--white);position:relative}
.section{position:absolute;left:0;width:1200px}
.abs{position:absolute}
.red{color:var(--red)}
.photo{position:absolute}

/* header + hero */
.hero{top:0;height:562px;background:linear-gradient(100deg,#2a2a2a 0%,#4a4a4a 45%,#8a8a8a 75%,#b8b4ad 100%)}
.hero .photo{inset:0}
.hero-shade{position:absolute;inset:0;background:linear-gradient(90deg,rgba(0,0,0,.55),rgba(0,0,0,0) 60%)}
.brand-name{color:var(--white);font-weight:700;letter-spacing:.5px;line-height:1.1}
.hero .brand-name{left:117px;top:32px;font-size:18px}
.nav{left:513px;top:42px;display:flex;gap:14px;align-items:center;font-size:11px;font-weight:700;color:var(--white)}
.nav .phone{display:flex;gap:5px;align-items:center}
.btn-red{background:var(--red);color:var(--white);font-weight:700;display:flex;align-items:center;justify-content:center}
.nav .btn-red{width:134px;height:28px;font-size:11px}
.hero h1{left:117px;top:195px;font-size:43px;line-height:41px;font-weight:400;color:var(--white)}
.hero h1 b{font-weight:700}
.hero p{left:117px;top:338px;width:410px;font-size:13px;line-height:19px;color:var(--white)}
.btn-outline{border:2px solid var(--white);color:var(--white);font-size:12px;font-weight:500;display:flex;align-items:center;justify-content:center}
.entry-split{left:117px;top:401px;display:flex;gap:12px}
.entry-split .btn-outline{width:169px;height:40px}
.entry-split .btn-red{width:169px;height:40px;font-size:12px;font-weight:500}

/* brands */
.brands{top:562px;height:177px;background:var(--white)}
.brands h2{top:20px;width:100%;text-align:center;font-size:15px;font-weight:500}
.brand-row{left:117px;top:85px;width:966px;display:flex;justify-content:space-between;align-items:center}
.brand-row span{font-size:20px;font-weight:700;color:var(--brand-ink)}

/* services */
.services{top:739px;height:614px;background:var(--dark);color:var(--white)}
.services h2{top:52px;width:100%;text-align:center;font-size:23px;font-weight:800}
.services p{left:160px;top:106px;width:880px;text-align:center;font-size:13px;line-height:22px}
.appliances{left:117px;top:240px;width:966px;display:flex;justify-content:space-between}
.appliance{width:180px;text-align:center;position:relative}
.appliance+.appliance::before{content:"";position:absolute;left:-12px;top:0;height:200px;width:1px;background:#333}
.appliance .photo{position:relative;margin:0 auto;width:130px;height:190px;background:linear-gradient(160deg,#fafafa,#c9c9c9)}
.appliance h3{margin-top:25px;font-size:13px;font-weight:600}
.appliance a{display:block;margin-top:6px;font-size:8px;font-weight:700;color:var(--red)}
.services .btn-red{left:520px;top:537px;width:183px;height:38px;font-size:13px}

/* why choose */
.why{top:1353px;height:434px;background:var(--grey-bg)}
.why h2{left:118px;top:40px;font-size:24px;font-weight:800}
.why-card{top:111px;width:311px;height:278px;background:var(--white);overflow:hidden}
.why-card .corner{position:absolute;right:0;top:0;width:107px;height:112px;background:var(--red);border-bottom-left-radius:100%}
.why-card h3{position:absolute;left:18px;top:68px;font-size:19px;line-height:24px;font-weight:700}
.why-card p{position:absolute;left:18px;top:133px;width:275px;font-size:11px;line-height:17px;color:#333}
.why-card p+p{top:200px}

/* testimonials */
.reviews{top:1787px;height:570px;background:linear-gradient(180deg,#3a3a3a,#1f1f1f 60%,#2c2c2c)}
.reviews .photo{inset:0}
.reviews h2{top:46px;width:100%;text-align:center;font-size:27px;line-height:37px;font-weight:700;color:var(--white)}
.reviews .sub{top:138px;width:100%;text-align:center;font-size:14px;color:#eee}
.review{top:215px;height:224px;border:2px solid var(--white);color:var(--white);padding:22px 28px}
.review h3{font-size:15px;font-weight:700}
.review .stars{color:#f6c21b;font-size:11px;letter-spacing:1px;margin:2px 0 10px}
.review p{font-size:12px;line-height:20.5px}
.arrow{top:313px;width:26px;height:26px;border-radius:50%;background:var(--red);display:flex;align-items:center;justify-content:center}
.reviews .btn-outline{left:515px;top:487px;width:140px;height:34px;font-size:13px;border-width:1.5px}

/* faq */
.faq{top:2357px;height:363px;background:var(--white)}
.faq h2{left:115px;top:47px;font-size:21px;font-weight:700}
.faq-list{left:117px;top:108px;width:717px}
.faq-item{height:66px;border-top:1px solid var(--line);display:flex;align-items:center;justify-content:space-between;font-size:16px;padding:0 2px}
.faq-item:last-child{border-bottom:1px solid var(--line)}
.faq-item b{color:var(--red);font-weight:700}
.faq-item .plus{font-size:22px;font-weight:400;margin-right:12px}
.request-box{left:865px;top:41px;width:207px;height:269px;background:var(--red);color:var(--white);overflow:hidden}
.request-box .big{position:absolute;left:13px;top:18px;font-size:31px;font-weight:800;line-height:1}
.request-box .mid{position:absolute;left:13px;top:54px;font-size:21px;font-weight:700}
.request-box .small{position:absolute;left:16px;top:91px;font-size:12px;font-weight:600}
.request-box .small2{position:absolute;left:16px;top:108px;font-size:15px;font-weight:600;z-index:1}
.request-box .photo{right:0;top:132px;width:100px;height:137px;background:linear-gradient(180deg,#c81b20,#8f1014)}
.request-box .cta{position:absolute;left:13px;top:189px;width:93px;height:28px;background:#ffd400;color:var(--ink);font-size:11px;font-weight:700;display:flex;align-items:center;justify-content:center}

/* contact */
.contact{top:2720px;height:531px;background:linear-gradient(110deg,#5a5650,#8a857c 45%,#b7b1a6 75%,#6d6a64)}
.contact .photo{inset:0}
.form-card{left:117px;top:76px;width:410px;height:416px;background:var(--white);padding:0 18px}
.form-card h2{margin-top:22px;font-size:34px;line-height:39px;font-weight:800}
.form-card p{margin-top:14px;font-size:13px;line-height:19px;width:330px}
.fields{margin-top:14px;display:grid;grid-template-columns:1fr 1fr;gap:11px 6px}
.field{height:42px;border:1px solid #999;font-size:11px;padding:13px 14px}
.field.wide{grid-column:1/3;height:76px}
.form-card .btn-red{margin-top:11px;height:41px;font-size:15px}

/* blogs */
.blogs{top:3251px;height:519px;background:var(--white)}
.blogs h2{left:118px;top:50px;font-size:28px;font-weight:800}
.blogs .sub{left:118px;top:89px;font-size:14px}
.view-all{left:987px;top:64px;display:flex;gap:8px;align-items:center;font-size:11px;font-weight:700;color:var(--red)}
.blog{top:142px;width:311px}
.blog .photo{position:relative;width:311px;height:234px}
.blog h3{margin:28px 0 0 6px;font-size:17px;line-height:22px;font-weight:700}
.blog a{display:block;margin:18px 0 0 6px;font-size:10px;font-weight:700;color:var(--red)}

/* footer */
.footer{top:3770px;height:297px;background:#1c1c1c;color:var(--white)}
.footer .brand-name{left:140px;top:76px;width:230px;font-size:29px;text-align:center}
.footer .brand-name span{font-size:20px;font-weight:700}
.socials{left:205px;top:146px;display:flex;gap:5px}
.socials i{width:27px;height:27px;border:1.5px solid var(--white);border-radius:50%;display:block}
.foot-col{top:42px;font-size:11px;line-height:23px}
.foot-col h4{font-size:11px;font-weight:700;margin-bottom:10px}
.contact-row{display:flex;gap:14px;align-items:center;margin-bottom:10px}
.contact-row .ico{width:27px;height:27px;border:1.5px solid var(--white);border-radius:50%;display:flex;align-items:center;justify-content:center}
.copyright{position:absolute;top:250px;width:100%;text-align:center;font-size:11px;color:#ddd}
.cut{position:absolute;background:var(--white)}
</style>
</head>
<body>

<header class="section hero">
  <div class="photo" role="img" aria-label="Technician inspecting a range hood in a modern kitchen"></div>
  <div class="hero-shade"></div>
  <div class="abs brand-name">TALL PINE<br>APPLIANCE CARE</div>
  <nav class="abs nav">
    <span>SERVICES</span><span>BRANDS</span><span>REVIEWS</span><span>BLOG</span><span>CONTACT</span>
    <span class="phone"><svg width="12" height="12" viewBox="0 0 24 24"><path fill="#fff" d="M6.6 10.8a15 15 0 0 0 6.6 6.6l2.2-2.2a1 1 0 0 1 1-.25 11.4 11.4 0 0 0 3.6.57 1 1 0 0 1 1 1V20a1 1 0 0 1-1 1A17 17 0 0 1 3 4a1 1 0 0 1 1-1h3.5a1 1 0 0 1 1 1c0 1.25.2 2.45.57 3.57a1 1 0 0 1-.25 1z"/></svg>431-555-0142</span>
    <span class="btn-red">REQUEST A REPAIR</span>
  </nav>
  <h1 class="abs">APPLIANCE <b>REPAIR</b><br>&amp; MAINTENANCE IN<br>WINNIPEG</h1>
  <p class="abs">Welcome to Tall Pine Appliance Care – your go-to for fast, reliable, and budget-friendly appliance repairs.</p>
  <div class="abs entry-split">
    <div class="btn-outline">RESIDENTIAL REPAIR</div>
    <div class="btn-red">COMMERCIAL REPAIR</div>
  </div>
</header>

<section class="section brands">
  <h2 class="abs">BRANDS WE <span class="red">REPAIR</span></h2>
  <div class="abs brand-row">
    <span>Frostline</span><span>Brann</span><span>Lumo</span><span>Tessa</span><span>Halden</span><span>Coldwell</span><span>Norvik</span><span>Eddyline</span>
  </div>
</section>

<section class="section services">
  <h2 class="abs">YOUR <span class="red">ONE-STOP</span> APPLIANCE SERVICES</h2>
  <p class="abs">With a decade of dedicated experience, Tall Pine Appliance Care delivers reliable and professional repairs for commercial and residential appliances. Our seasoned technicians specialize in fixing appliances from any brand and offer a three-month warranty on all repairs.</p>
  <div class="abs appliances">
    <div class="appliance"><div class="photo" role="img" aria-label="White front-load washer"></div><h3>WASHER</h3><a>LEARN MORE</a></div>
    <div class="appliance"><div class="photo" role="img" aria-label="White front-load dryer"></div><h3>DRYER</h3><a>LEARN MORE</a></div>
    <div class="appliance"><div class="photo" role="img" aria-label="White top-freezer refrigerator"></div><h3>REFRIGERATOR</h3><a>LEARN MORE</a></div>
    <div class="appliance"><div class="photo" role="img" aria-label="White electric range with oven"></div><h3>OVEN &amp; STOVE</h3><a>LEARN MORE</a></div>
    <div class="appliance"><div class="photo" role="img" aria-label="White built-in dishwasher"></div><h3>DISHWASHER</h3><a>LEARN MORE</a></div>
  </div>
  <div class="abs btn-red">CONTACT US NOW</div>
</section>

<section class="section why">
  <h2 class="abs">WHY <span class="red">CHOOSE</span> US?</h2>
  <div class="abs why-card" style="left:117px"><div class="corner"></div><h3>REPAIR ON THE<br>SAME DAY</h3><p>At Tall Pine Appliance Care, we understand the urgency of getting your appliances back in action.</p><p>Our commitment to prompt service ensures that we offer same-day repairs to minimize disruptions in your daily routine.</p></div>
  <div class="abs why-card" style="left:444px"><div class="corner"></div><h3>SATISFACTION<br>GUARANTEED</h3><p>Our skilled technicians are dedicated to delivering top-notch appliance repairs, ensuring that your devices function optimally.</p></div>
  <div class="abs why-card" style="left:771px"><div class="corner"></div><h3>10 YEAR<br>EXPERIENCE</h3><p>Over the past decade, we've successfully resolved a myriad of appliance issues, earning the trust of our valued customers.</p></div>
</section>

<section class="section reviews">
  <div class="photo" role="img" aria-label="Dim workshop scene with a technician's hands at work"></div>
  <h2 class="abs">HERE'S WHAT OUR SATISFIED<br>CUSTOMERS ARE SAYING...</h2>
  <div class="abs sub">we take pride in providing exceptional insulation service to our customers.</div>
  <div class="abs arrow" style="left:104px"><svg width="10" height="10" viewBox="0 0 10 10"><path d="M6.5 1.5 3 5l3.5 3.5" fill="none" stroke="#fff" stroke-width="1.5"/></svg></div>
  <div class="abs review" style="left:141px;width:431px"><h3>Corinne L</h3><div class="stars">★★★★★</div><p>"My oven malfunctioned on the holiday eve. I anticipated hosting a large dinner for numerous guests. I promptly contacted Tall Pine Appliance Care, and they responded within 2 hours and saved this situation. There have been no problems since. Everything has been functioning flawlessly."</p></div>
  <div class="abs review" style="left:589px;width:433px"><h3>Martin Okafor</h3><div class="stars">★★★★★</div><p>"Tall Pine Appliance Care technician Devin exhibited friendliness and profound knowledge while assessing my washing machine. He inquired extensively to grasp the nature of the issue. His thorough approach left me confident that the issue was resolved, and he also provided valuable advice. I plan to reach out to Tall Pine Appliance Care again."</p></div>
  <div class="abs arrow" style="left:1042px"><svg width="10" height="10" viewBox="0 0 10 10"><path d="M3.5 1.5 7 5 3.5 8.5" fill="none" stroke="#fff" stroke-width="1.5"/></svg></div>
  <div class="abs btn-outline">SEE ALL</div>
</section>

<section class="section faq">
  <h2 class="abs">FREQUENTLY <span class="red">ASKED</span> QUESTIONS</h2>
  <div class="abs faq-list">
    <div class="faq-item"><span><b>Q:</b> Why do I need to pay for a service call (diagnostics)?</span><span class="plus">+</span></div>
    <div class="faq-item"><span><b>Q:</b> How much warranty do I have for a replaced part?</span><span class="plus">+</span></div>
    <div class="faq-item"><span><b>Q:</b> If a customer proceeds with the repair, does he need to pay for diagnostics?</span><span class="plus">+</span></div>
  </div>
  <div class="abs request-box">
    <div class="big">REQUEST</div><div class="mid">A REPAIR</div>
    <div class="small">Report It Today.</div><div class="small2">Relax Tomorrow.</div>
    <div class="photo" role="img" aria-label="Technician in red uniform beside a washer"></div>
    <div class="cta">CLICK HERE</div>
  </div>
</section>

<section class="section contact">
  <div class="photo" role="img" aria-label="Smiling technician servicing an open dishwasher in a modern kitchen"></div>
  <div class="abs form-card">
    <h2>CALL OR EMAIL<br>US TODAY</h2>
    <p>Connect with us today to explore how our expertise can help you with your repair needs.</p>
    <div class="fields">
      <div class="field">First Name</div><div class="field">Last Name</div>
      <div class="field">Email Address</div><div class="field">Phone Number</div>
      <div class="field wide">Message</div>
    </div>
    <div class="btn-red">SUBMIT</div>
  </div>
</section>

<section class="section blogs">
  <h2 class="abs">LATEST BLOGS</h2>
  <div class="abs sub">Where Knowledge Meets Innovation.</div>
  <div class="abs view-all">VIEW ALL <svg width="24" height="12" viewBox="0 0 24 12"><path d="M6 1 1 6l5 5M18 1l5 5-5 5" fill="none" stroke="#e31e24" stroke-width="1.5"/></svg></div>
  <article class="abs blog" style="left:117px"><div class="photo" role="img" aria-label="Gas range burner with blue flame" style="background:linear-gradient(160deg,#e9d2a8,#3d6fb0)"></div><h3>Gas Range Maintenance Tips for Longevity and Performance</h3><a>LEAR MORE</a></article>
  <article class="abs blog" style="left:444px"><div class="photo" role="img" aria-label="Inside of a glowing oven" style="background:linear-gradient(160deg,#3a2214,#d8822e)"></div><h3>Top Reasons Your Gas Oven Isn't Heating Properly</h3><a>LEAR MORE</a></article>
  <article class="abs blog" style="left:771px"><div class="photo" role="img" aria-label="Close view of a gas stove burner" style="background:linear-gradient(160deg,#f0dcb0,#2c4f86)"></div><h3>Common Issues with Gas Stoves and How to Troubleshoot Them</h3><a>LEAR MORE</a></article>
</section>

<footer class="section footer">
  <div class="cut" style="left:1150px;top:0;width:50px;height:110px;clip-path:polygon(100% 0,100% 100%,0 60%)"></div>
  <div class="cut" style="left:0;top:170px;width:55px;height:127px;clip-path:polygon(0 0,100% 65%,60% 100%,0 100%)"></div>
  <div class="abs brand-name">TALL PINE<br><span>APPLIANCE CARE</span></div>
  <div class="abs socials"><i></i><i></i></div>
  <div class="abs foot-col" style="left:425px"><h4>NAVIGATION</h4>Services<br>Brands<br>Reviews<br>FAQ<br>Kontakt</div>
  <div class="abs foot-col" style="left:576px"><h4>SERVICES WE OFFER</h4>Dryer Repair<br>Washer Repair<br>Stove &amp; Oven Repair<br>Refrigerator Repair<br>Dishwasher Repair<br>Commercial Appliances Repair</div>
  <div class="abs foot-col" style="left:828px"><h4 style="margin-left:45px">CONTACT US</h4>
    <div class="contact-row"><span class="ico"><svg width="12" height="12" viewBox="0 0 24 24"><path fill="#fff" d="M6.6 10.8a15 15 0 0 0 6.6 6.6l2.2-2.2a1 1 0 0 1 1-.25 11.4 11.4 0 0 0 3.6.57 1 1 0 0 1 1 1V20a1 1 0 0 1-1 1A17 17 0 0 1 3 4a1 1 0 0 1 1-1h3.5a1 1 0 0 1 1 1c0 1.25.2 2.45.57 3.57a1 1 0 0 1-.25 1z"/></svg></span><span style="font-size:17px;font-weight:700">431-555-0142</span></div>
    <div class="contact-row"><span class="ico"><svg width="13" height="10" viewBox="0 0 13 10"><rect x=".5" y=".5" width="12" height="9" fill="none" stroke="#fff"/><path d="M.5.5 6.5 5.5 12.5.5" fill="none" stroke="#fff"/></svg></span><span style="font-size:12px">tallpineappliancecare.ca</span></div>
    <div class="contact-row"><span class="ico"><svg width="10" height="13" viewBox="0 0 10 13"><path d="M5 12.5S1 7.5 1 5a4 4 0 0 1 8 0c0 2.5-4 7.5-4 7.5z" fill="none" stroke="#fff"/><circle cx="5" cy="5" r="1.4" fill="#fff"/></svg></span><span>Winnipeg, MB, Canada</span></div>
  </div>
  <div class="copyright">© 2026 Tall Pine Appliance Care &nbsp;|&nbsp; Privacy Policy</div>
</footer>

</body>
</html>
```